pop up booking component and calendar re-design

we have a calander view where a parent cant reserve a day
you can click on please redesign the calander / voucher and pop up.

the dropdowns in pop up can be buttons
the dots on the calander indicate if there is space or not

when booking a day you can select a voucher

we used MELO as inspiration, you are welcome to look at it as well.. screenshots attached

please ask questions if you have any

```html
<!DOCTYPE html>
<html lang="en">
<head>
<meta charset="utf-8">
<title>Booking calendar and voucher panel</title>
<link href="https://fonts.googleapis.com/css2?family=Play:wght@400;700&display=swap" rel="stylesheet">
<style>
:root{
  --page:#ffffff;
  --panel:#ffffff;
  --ink:#1f2630;
  --day-open:#8fd0f8;
  --day-open-ink:#243246;
  --day-full:#46536a;
  --day-past:#8a9198;
  --day-booked:#7ed321;
  --today-ring:#e8643a;
  --side:#2b3238;
  --side-head:#242c3b;
  --side-ink:#ffffff;
  --side-rule:#4a535b;
  --link:#2f8bff;
  --btn-muted:#8fd0f8;
  --btn-grey:#8a9198;
  --btn-red:#dc3545;
  --btn-dark:#272d33;
  --accent:#1fb6d9;
  --popup:#ededed;
}
*{box-sizing:border-box;margin:0;padding:0}
html,body{width:815px;height:1200px;overflow:hidden;background:var(--page)}
body{position:relative;font-family:"Play",sans-serif;color:var(--ink)}
.panel{position:absolute;width:711px;height:355px;background:var(--panel);box-shadow:0 0 6px rgba(0,0,0,.08);overflow:hidden}
.panel--hero{left:123px;top:66px;transform:scale(.8);transform-origin:0 0}
.panel--plain{left:49px;top:423px}
.panel--popup{left:50px;top:802px}
.month-nav{position:absolute;top:18px;left:64px;width:394px;display:flex;justify-content:space-between;align-items:center;font-size:10px}
.month-nav .current{font-size:12.5px;font-weight:700;letter-spacing:.3px}
.calendar{position:absolute;left:43px;top:48px;display:grid;grid-template-columns:repeat(7,63px);grid-auto-rows:42px}
.calendar .weekday{height:20px;align-self:start;text-align:center;font-size:9.5px}
.calendar .weekdays{display:contents}
.day{justify-self:center;align-self:center;width:25px;height:25px;border-radius:50%;display:flex;align-items:center;justify-content:center;font-size:10px;box-shadow:0 1px 2px rgba(0,0,0,.2)}
.day--open{background:var(--day-open);color:var(--day-open-ink)}
.day--full{background:var(--day-full);color:#fff}
.day--past{background:var(--day-past);color:#fff}
.day--booked{background:var(--day-booked);color:var(--day-open-ink)}
.day--today{background:#fff;border:1.5px solid var(--today-ring);color:var(--day-open-ink)}
.day-row{display:contents}
.weekrow-gap{height:0}
.actions{position:absolute;top:305px;left:62px;display:flex;gap:8px}
.actions button{width:93px;height:28px;border:0;color:#fff;font-family:inherit;font-size:10px;display:flex;align-items:center;justify-content:center;gap:4px;box-shadow:0 1px 2px rgba(0,0,0,.2)}
.btn-not-coming{background:var(--btn-muted)}
.btn-unselect{background:var(--btn-grey)}
.btn-cancel{background:var(--btn-red)}
.btn-reset{background:var(--btn-dark)}
.vouchers{position:absolute;left:519px;top:0;width:192px;height:100%;background:var(--side);color:var(--side-ink);padding:22px 10px 0 11px;font-size:8.6px}
.vouchers h2{height:29px;background:var(--side-head);display:flex;align-items:center;justify-content:center;font-size:10px;font-weight:700;box-shadow:0 1px 3px rgba(0,0,0,.35)}
.vouchers .purchase-head{margin-top:17px;display:flex;align-items:center;gap:4px;color:var(--link);font-size:9px;padding-bottom:11px;border-bottom:1px solid var(--side-rule)}
.badge{width:13px;height:13px;border-radius:50%;background:var(--day-booked);color:#fff;font-size:7px;display:flex;align-items:center;justify-content:center}
.offer{padding:9px 0 8px;border-bottom:1px solid var(--side-rule);display:grid;grid-template-columns:1fr auto;row-gap:11px}
.offer:last-of-type{border-bottom:0}
.offer .right{text-align:right}
.offer a{color:#fff;text-decoration:underline}
.offer s{margin-right:2px}
.vouchers .code{position:absolute;right:5px;bottom:23px;font-size:9px}
.booking{position:absolute;left:86px;top:149px;width:346px;height:136px;background:var(--popup);box-shadow:0 1px 4px rgba(0,0,0,.25);font-size:9px}
.tabs{position:absolute;left:16px;top:5px;width:315px;height:19px;border-bottom:1px solid #c9c9c9;display:flex;align-items:flex-end}
.tab{height:19px;padding:0 4px;display:flex;align-items:center}
.tab--active{border:1px solid #c9c9c9;border-bottom:1px solid var(--popup);background:var(--popup);margin-bottom:-1px}
.tab+.tab{margin-left:10px}
.avail{position:absolute;left:16px;top:32px;display:flex;gap:23px}
.field-labels{position:absolute;left:16px;top:51px;width:214px;height:14px}
.field-labels span{position:absolute;top:0}
.req{color:var(--btn-red)}
.toggle{position:absolute;left:185px;top:50px;width:43px;height:16px;border-radius:8px;background:#d5d5d5}
.toggle::before{content:"";position:absolute;left:1px;top:1px;width:14px;height:14px;border-radius:50%;background:#fff;box-shadow:0 1px 2px rgba(0,0,0,.3)}
.select{position:absolute;top:67px;height:16px;border:1px solid #bbb;background:#fff;font-size:6.5px;display:flex;align-items:center;justify-content:space-between;padding:0 5px}
.select::after{content:"";border:3px solid transparent;border-top:3.5px solid #333;margin-top:3px}
.sessions{position:absolute;left:16px;top:89px;display:flex;gap:1px}
.sessions span{height:16px;border:1px solid var(--accent);background:#fff;color:var(--accent);font-size:7px;font-weight:700;display:flex;align-items:center;justify-content:space-between;padding:0 4px 0 8px}
.sessions .on{background:var(--accent);color:#fff}
.sessions .count{color:var(--ink)}
.sessions .on .count{color:#fff}
.btn-close{position:absolute;left:16px;top:111px;width:66px;height:17px;border:0;background:var(--btn-red);color:#fff;font-family:inherit;font-size:7.5px;font-weight:700}
.summary{position:absolute;left:241px;top:25px;width:90px;height:98px;background:#fff;padding:0 8px}
.summary .line{display:flex;justify-content:space-between;height:24px;align-items:center;border-bottom:1px solid #ddd}
.summary .line:nth-child(3){border-bottom:0;height:28px}
.summary a{color:var(--accent);text-decoration:underline}
.btn-confirm{display:block;width:66px;height:16px;margin-left:8px;border:0;background:var(--accent);color:#fff;font-family:inherit;font-size:7.5px;font-weight:700}
</style>
</head>
<body>

<!-- Calendar overview -->
<section class="panel panel--hero">
  <header class="month-nav"><span>Sep 2019</span><span class="current">OCTOBER 2019</span><span>Nov 2019</span></header>
  <div class="calendar">
    <span class="weekday">SUN</span><span class="weekday">MON</span><span class="weekday">TUE</span><span class="weekday">WED</span><span class="weekday">THU</span><span class="weekday">FRI</span><span class="weekday">SAT</span>
    <span></span><span></span><span class="day day--open">01</span><span class="day day--open">02</span><span class="day day--past">03</span><span class="day day--past">04</span><span class="day day--full">05</span>
    <span class="day day--full">06</span><span class="day day--open">07</span><span class="day day--open">08</span><span class="day day--open">09</span><span class="day day--past">10</span><span class="day day--past">11</span><span class="day day--full">12</span>
    <span class="day day--full">13</span><span class="day day--open">14</span><span class="day day--open">15</span><span class="day day--today">16</span><span class="day day--booked">17</span><span class="day day--booked">18</span><span class="day day--full">19</span>
    <span class="day day--full">20</span><span class="day day--open">21</span><span class="day day--open">22</span><span class="day day--open">23</span><span class="day day--booked">24</span><span class="day day--booked">25</span><span class="day day--full">26</span>
    <span class="day day--full">27</span><span class="day day--open">28</span><span class="day day--past">29</span><span class="day day--past">30</span><span class="day day--booked">31</span>
  </div>
  <div class="actions">
    <button class="btn-not-coming">Not Coming</button><button class="btn-unselect">Unselect</button><button class="btn-cancel">Cancel</button>
    <button class="btn-reset"><svg width="9" height="9" viewBox="0 0 16 16" fill="none" stroke="#fff" stroke-width="2.4"><path d="M13 6a5.5 5.5 0 0 0-10-1M3 10a5.5 5.5 0 0 0 10 1"/><path d="M2 1v4h4M14 15v-4h-4"/></svg>Reset</button>
  </div>
  <aside class="vouchers">
    <h2>Voucher / Promotions</h2>
    <div class="purchase-head">Purchase <span class="badge">2</span></div>
    <div class="offer"><span>Booking Test Prom</span><span class="right">10 Hours @ € 8.9</span><span>Valid Till 15th Dec 2019</span><span class="right">0 / 10</span><span>€ 89.00</span><a class="right">Purchase</a></div>
    <div class="offer"><span>Test Lab Prom</span><span class="right">10 Hours @ € 8.93</span><span>Valid Till 14th Jan 2020</span><span class="right">0 / 10</span><span><s>€ 89.30</s> € 80.37</span><a class="right">Purchase</a></div>
    <span class="code">C29</span>
  </aside>
</section>

<!-- Calendar with voucher panel -->
<section class="panel panel--plain">
  <header class="month-nav"><span>Sep 2019</span><span class="current">OCTOBER 2019</span><span>Nov 2019</span></header>
  <div class="calendar">
    <span class="weekday">SUN</span><span class="weekday">MON</span><span class="weekday">TUE</span><span class="weekday">WED</span><span class="weekday">THU</span><span class="weekday">FRI</span><span class="weekday">SAT</span>
    <span></span><span></span><span class="day day--open">01</span><span class="day day--open">02</span><span class="day day--past">03</span><span class="day day--past">04</span><span class="day day--full">05</span>
    <span class="day day--full">06</span><span class="day day--open">07</span><span class="day day--open">08</span><span class="day day--open">09</span><span class="day day--past">10</span><span class="day day--past">11</span><span class="day day--full">12</span>
    <span class="day day--full">13</span><span class="day day--open">14</span><span class="day day--open">15</span><span class="day day--today">16</span><span class="day day--booked">17</span><span class="day day--booked">18</span><span class="day day--full">19</span>
    <span class="day day--full">20</span><span class="day day--open">21</span><span class="day day--open">22</span><span class="day day--open">23</span><span class="day day--booked">24</span><span class="day day--booked">25</span><span class="day day--full">26</span>
    <span class="day day--full">27</span><span class="day day--open">28</span><span class="day day--past">29</span><span class="day day--past">30</span><span class="day day--booked">31</span>
  </div>
  <div class="actions">
    <button class="btn-not-coming">Not Coming</button><button class="btn-unselect">Unselect</button><button class="btn-cancel">Cancel</button>
    <button class="btn-reset"><svg width="9" height="9" viewBox="0 0 16 16" fill="none" stroke="#fff" stroke-width="2.4"><path d="M13 6a5.5 5.5 0 0 0-10-1M3 10a5.5 5.5 0 0 0 10 1"/><path d="M2 1v4h4M14 15v-4h-4"/></svg>Reset</button>
  </div>
  <aside class="vouchers">
    <h2>Voucher / Promotions</h2>
    <div class="purchase-head">Purchase <span class="badge">2</span></div>
    <div class="offer"><span>Booking Test Prom</span><span class="right">10 Hours @ € 8.9</span><span>Valid Till 15th Dec 2019</span><span class="right">0 / 10</span><span>€ 89.00</span><a class="right">Purchase</a></div>
    <div class="offer"><span>Test Lab Prom</span><span class="right">10 Hours @ € 8.93</span><span>Valid Till 14th Jan 2020</span><span class="right">0 / 10</span><span><s>€ 89.30</s> € 80.37</span><a class="right">Purchase</a></div>
    <span class="code">C29</span>
  </aside>
</section>

<!-- Calendar with booking dialog -->
<section class="panel panel--popup">
  <header class="month-nav"><span>Sep 2019</span><span class="current">OCTOBER 2019</span><span>Nov 2019</span></header>
  <div class="calendar">
    <span class="weekday">SUN</span><span class="weekday">MON</span><span class="weekday">TUE</span><span class="weekday">WED</span><span class="weekday">THU</span><span class="weekday">FRI</span><span class="weekday">SAT</span>
    <span></span><span></span><span class="day day--open">01</span><span class="day day--open">02</span><span class="day day--past">03</span><span class="day day--past">04</span><span class="day day--full">05</span>
    <span class="day day--full">06</span><span class="day day--open">07</span><span class="day day--open">08</span><span class="day day--open">09</span><span class="day day--past">10</span><span class="day day--past">11</span><span class="day day--full">12</span>
    <span class="day day--full">13</span><span class="day day--open">14</span><span class="day day--open">15</span><span class="day day--today">16</span><span class="day day--booked">17</span><span class="day day--booked">18</span><span class="day day--full">19</span>
    <span class="day day--full">20</span><span class="day day--open">21</span><span class="day day--open">22</span><span class="day day--open">23</span><span class="day day--booked">24</span><span class="day day--booked">25</span><span class="day day--full">26</span>
    <span class="day day--full">27</span><span class="day day--open">28</span><span class="day day--past">29</span><span class="day day--past">30</span><span class="day day--booked">31</span>
  </div>
  <div class="actions">
    <button class="btn-not-coming">Not Coming</button><button class="btn-unselect">Unselect</button><button class="btn-cancel">Cancel</button>
    <button class="btn-reset"><svg width="9" height="9" viewBox="0 0 16 16" fill="none" stroke="#fff" stroke-width="2.4"><path d="M13 6a5.5 5.5 0 0 0-10-1M3 10a5.5 5.5 0 0 0 10 1"/><path d="M2 1v4h4M14 15v-4h-4"/></svg>Reset</button>
  </div>

  <div class="booking">
    <nav class="tabs"><span class="tab tab--active">Book Day</span><span class="tab">Vouchers</span></nav>
    <div class="avail"><span>Availability - 1m / 1a left</span><span>24 - 10 - 2019</span></div>
    <div class="field-labels">
      <span style="left:0">Locations <span class="req">*</span></span>
      <span style="left:78px">Groups <span class="req">*</span></span>
      <span style="left:145px">BSO</span>
    </div>
    <span class="toggle"></span>
    <div class="select" style="left:16px;width:66px">RBW</div>
    <div class="select" style="left:95px;width:65px">3 - Penguins</div>
    <div class="sessions">
      <span class="on" style="width:42px">Full <span class="count">1</span></span>
      <span style="width:41px">AM <span class="count">1</span></span>
      <span style="width:42px">PM <span class="count">1</span></span>
      <span style="width:42px;justify-content:center;padding:0">FLEX</span>
      <span style="width:42px;justify-content:center;padding:0">TRY</span>
    </div>
    <button class="btn-close">Close</button>
    <div class="summary">
      <div class="line"><span>Price</span><span>€ 98.23</span></div>
      <div class="line"><span>Voucher</span><a>Apply</a></div>
      <div class="line"><span>Total</span><span>€ 98.23</span></div>
      <button class="btn-confirm">Confirm</button>
    </div>
  </div>

  <aside class="vouchers">
    <h2>Voucher / Promotions</h2>
    <div class="purchase-head">Purchase <span class="badge">2</span></div>
    <div class="offer"><span>Booking Test Prom</span><span class="right">10 Hours @ € 8.9</span><span>Valid Till 15th Dec 2019</span><span class="right">0 / 10</span><span>€ 89.00</span><a class="right">Purchase</a></div>
    <div class="offer"><span>Test Lab Prom</span><span class="right">10 Hours @ € 8.93</span><span>Valid Till 14th Jan 2020</span><span class="right">0 / 10</span><span><s>€ 89.30</s> € 80.37</span><a class="right">Purchase</a></div>
    <span class="code">C29</span>
  </aside>
</section>

</body>
</html>
```